Tallis Ecological Works New Website Design

I need a new website for a Environmental Project Company based in Sydney Australia, working throughout South East Asia.I've attached the company logo, please try & incorporate these colours or use complimentary colours. I've attached a word doc with design brief.I'm going to use Wix, so please ensure files are suitable.Thankyou.

Number of Pages Required

5+ page

Colors

Designer to choose colors to be used in the design.

Requirements
Must have
• Refer to Word Document
Nice to have
• Refer to Word Document
Should not have
• Not to be dark

```html
<!DOCTYPE html>
<html lang="en">
<head>
<meta charset="utf-8">
<title>Tallis Ecological Works</title>
<link href="https://fonts.googleapis.com/css2?family=Cinzel:wght@400;500&family=Poppins:wght@300;400;500;600&display=swap" rel="stylesheet">
<style>
:root{
  --green:#4a6b25;
  --green-dark:#3f5d1f;
  --teal:#0fa88c;
  --mint:#e6fbf8;
  --text:#333;
  --muted:#666;
  --white:#fff;
  --client:#6d6d6d;
}
*{box-sizing:border-box;margin:0;padding:0}
html,body{width:1200px;height:4199px;overflow:hidden}
body{position:relative;font-family:"Poppins",sans-serif;color:var(--text);background:var(--white)}
.abs{position:absolute}
.heading{font-family:"Cinzel",serif;font-weight:400;letter-spacing:1px}
.rule{position:absolute;width:42px;height:3px;background:var(--teal);left:50%;margin-left:-21px}
.btn{position:absolute;background:var(--teal);color:#fff;font-size:12px;display:flex;align-items:center;justify-content:center;white-space:nowrap}
.center{text-align:center;left:0;width:1200px}

.topbar{top:0;left:0;width:1200px;height:33px;background:var(--green);color:#fff;font-size:11px}
.topbar span{position:absolute;top:10px;white-space:nowrap}
.dot{position:absolute;top:10px;width:12px;height:12px;border:1.5px solid #d8e2cc;border-radius:50%}
.header{top:33px;left:0;width:1200px;height:83px;background:#fff;border-bottom:1px solid #eee}
.logo-mark{position:absolute;left:108px;top:12px;width:60px;height:60px;border-radius:50%;background:var(--green)}
.logo-name{position:absolute;left:182px;top:14px;font-family:"Cinzel",serif;color:var(--green);font-size:17px;line-height:19px;letter-spacing:2px}
.logo-name small{display:block;font-size:9px;line-height:12px;letter-spacing:1px}
.nav span{position:absolute;top:34px;font-size:13px;color:#444;white-space:nowrap}
.nav .active{color:var(--teal)}

.hero-photo{top:116px;left:0;width:1200px;height:640px;background:linear-gradient(160deg,#b8c7cf 0%,#9fb0b6 35%,#5d7a45 65%,#3e5a2c 100%)}
.hero-panel{top:277px;left:0;width:600px;height:370px;background:rgba(74,107,37,.95);color:#fff}
.hero-panel h1{position:absolute;left:127px;top:65px;font-size:29px;line-height:40px}
.hero-panel p{position:absolute;left:127px;top:157px;width:360px;font-size:12.5px;line-height:24px}

.body-text{font-size:14.5px;line-height:30px;color:#444}
.mint-a{top:1105px;left:0;width:1200px;height:747px;background:var(--mint);clip-path:polygon(0 101px,1200px 0,1200px 747px,0 747px)}
.mint-b{top:2823px;left:0;width:1200px;height:616px;background:var(--mint);clip-path:polygon(0 0,1200px 0,1200px 616px,0 515px)}
.mission-item{position:absolute;width:290px;text-align:center;font-size:12.5px;color:#444;white-space:nowrap}
.mission-item svg{display:block;margin:0 auto 14px}

.band{left:0;width:1200px;background:var(--green);color:#fff}
.card-img{position:absolute;top:2196px;width:282px;height:187px}
.card-title{position:absolute;top:2406px;font-size:19px;color:#4a4a4a;white-space:nowrap}
.card-text{position:absolute;top:2442px;width:282px;font-size:11.5px;line-height:16.5px;color:#555}

.field{position:absolute;top:2720px;height:40px;background:#fff;font-size:12px;color:#999;padding:11px 14px}
.news-img{position:absolute;top:3007px;width:187px;height:185px}
.news-title{position:absolute;top:3025px;font-family:"Cinzel",serif;font-size:14px;line-height:18px;color:#555;letter-spacing:.5px;font-weight:400}
.news-text{position:absolute;top:3068px;width:200px;font-size:11.5px;line-height:20px;color:#555}
.news-more{position:absolute;top:3172px;font-size:11.5px;color:var(--teal)}

.clients{position:absolute;top:3586px;left:104px;width:992px;height:44px;display:flex;justify-content:space-between;align-items:center}
.client{width:150px;font-size:16px;font-weight:600;color:var(--client);display:flex;align-items:center;justify-content:center;gap:7px;white-space:nowrap}
.client i{flex:none;width:16px;height:16px;background:var(--client)}

.footer{top:3684px;left:0;width:1200px;height:515px;background:var(--green);color:#fff}
.f-label{position:absolute;font-family:"Cinzel",serif;font-size:12px;letter-spacing:.5px}
.f-city{position:absolute;font-family:"Cinzel",serif;font-size:16px;letter-spacing:1px}
.f-text{position:absolute;font-size:12px;line-height:20px;white-space:nowrap}
.f-ico{position:absolute;width:24px;height:24px;border:1.5px solid #fff;border-radius:50%}
.search{position:absolute;left:147px;top:68px;width:234px;height:36px;background:#fff;color:#999;font-size:11px;padding:10px 14px}
.f-links{position:absolute;left:822px;top:464px;display:flex;gap:22px;font-size:11px;line-height:20px}
</style>
</head>
<body>

<div class="abs topbar">
  <span style="left:676px">Investor Centre</span>
  <span style="left:783px">Media Centre</span>
  <span style="left:876px">Login</span>
  <span style="left:938px">AU</span>
  <i class="abs" style="left:964px;top:11px;width:16px;height:11px;background:#2a4d8f"></i>
  <i class="dot" style="left:1010px"></i><i class="dot" style="left:1040px"></i><i class="dot" style="left:1072px"></i>
</div>

<header class="abs header">
  <div class="logo-mark"></div>
  <div class="logo-name">TALLIS<small>ECOLOGICAL</small>WORKS</div>
  <nav class="nav">
    <span class="active" style="left:515px">HOME</span>
    <span style="left:592px">Who we are</span>
    <span style="left:704px">Services</span>
    <span style="left:795px">Products</span>
    <span style="left:889px">News</span>
    <span style="left:964px">Contact</span>
  </nav>
  <svg class="abs" style="left:1073px;top:32px" width="20" height="20" viewBox="0 0 20 20"><circle cx="8" cy="8" r="6" fill="none" stroke="#888" stroke-width="1.4"/><path d="M12.5 12.5 18 18" stroke="#888" stroke-width="1.4"/></svg>
</header>

<div class="abs hero-photo" role="img" aria-label="City avenue lined with green trees leading towards high-rise towers"></div>
<section class="abs hero-panel">
  <h1 class="heading">Changing Lives &amp;<br>Saving Planet Earth</h1>
  <p>Environmental Project Company based in Sydney Australia, working throughout South East Asia. Lorem ipsum dolor sit amet, consectetur.</p>
  <div class="btn" style="left:128px;top:259px;width:152px;height:40px">Learn more</div>
</section>

<section>
  <h2 class="abs heading center" style="top:832px;font-size:29px">Welcome!</h2>
  <div class="rule" style="top:876px"></div>
  <p class="abs center body-text" style="top:893px;padding:0 120px">Our Vision is to make it easy for everyone to minimise their environmental impact by providing information, technology, packaged green solutions &amp; helping innovation flourish. We can help you accelerate your sustainability journey with tailored, innovative and evidence-based solutions. We identify opportunities for you to deliver triple bottom line benefits based on a commitment to genuine life-cycle thinking.</p>
  <div class="btn" style="left:521px;top:1050px;width:158px;height:41px">more about us!</div>
</section>

<div class="abs mint-a"></div>
<section>
  <h2 class="abs heading center" style="top:1288px;font-size:29px">Our Mission</h2>
  <div class="rule" style="top:1333px"></div>
  <p class="abs center" style="top:1361px;font-size:13px;line-height:25px;color:#444">Working with people to minimise the environmental impact of humans on the earth<br>without sacrificing lifestyle and helping innovation flourish.<br>We will achieve this by focusing on the following:</p>

  <div class="mission-item" style="left:190px;top:1462px">
    <svg width="84" height="84" viewBox="0 0 84 84" fill="none" stroke="#0fa88c" stroke-width="3"><circle cx="40" cy="42" r="37"/><ellipse cx="40" cy="42" rx="16" ry="37"/><path d="M3 42h74M10 24h60M10 60h60M40 5v74"/><path d="M56 74c0-16 10-24 24-24-2 14-10 22-24 24z" fill="#e6fbf8"/></svg>
    Sustainable food</div>
  <div class="mission-item" style="left:441px;top:1462px">
    <svg width="60" height="96" viewBox="0 0 60 96" fill="none" stroke="#0fa88c" stroke-width="3"><path d="M30 3a26 26 0 0 0-16 46c4 4 5 8 5 14h22c0-6 1-10 5-14A26 26 0 0 0 30 3z"/><path d="M20 70h20M22 78h16M25 86h10M30 62V30"/><path d="M30 34c-8 0-12-6-12-12 8 0 12 6 12 12zM30 30c0-8 6-12 12-12 0 8-6 12-12 12z"/></svg>
    Sustainable / Renewable power</div>
  <div class="mission-item" style="left:692px;top:1462px">
    <svg width="84" height="84" viewBox="0 0 84 84" fill="none" stroke="#0fa88c" stroke-width="3"><circle cx="42" cy="30" r="18"/><path d="M45 18l-8 14h10l-8 12"/><path d="M42 3v5M20 10l4 4M64 10l-4 4M14 30h-5M75 30h-5"/><path d="M4 58c6-5 12-5 19 0s13 5 19 0 13-5 19 0 13 5 19 0M4 68c6-5 12-5 19 0s13 5 19 0 13-5 19 0 13 5 19 0M4 78c6-5 12-5 19 0s13 5 19 0 13-5 19 0 13 5 19 0"/></svg>
    Water quality &amp; treatment</div>

  <div class="mission-item" style="left:190px;top:1632px">
    <svg width="70" height="96" viewBox="0 0 70 96" fill="none" stroke="#0fa88c" stroke-width="3"><circle cx="35" cy="34" r="6"/><path d="M35 28c-6-10-4-22 0-26 4 4 6 16 0 26zM30 38c-12 0-20 8-22 14 6 2 16-2 22-14zM40 38c12 0 20 8 22 14-6 2-16-2-22-14z"/><path d="M35 40v44M26 84h18M22 92h26"/></svg>
    Air quality</div>
  <div class="mission-item" style="left:441px;top:1632px">
    <svg width="86" height="96" viewBox="0 0 86 96" fill="none" stroke="#0fa88c" stroke-width="3"><path d="M4 94h78"/><rect x="10" y="30" width="18" height="64"/><rect x="30" y="18" width="16" height="76"/><rect x="48" y="60" width="26" height="34"/><path d="M15 40h8M15 52h8M15 64h8M15 76h8M35 30h6M35 44h6M35 58h6M35 72h6M54 70h6M64 70h6M54 82h6M64 82h6"/><path d="M68 54V28M68 28l-10-6M68 28l10-6M68 28v12"/></svg>
    Investing in green infrastructure &amp; projects</div>
  <div class="mission-item" style="left:692px;top:1632px">
    <svg width="70" height="96" viewBox="0 0 70 96" fill="none" stroke="#0fa88c" stroke-width="3"><path d="M20 94V78C8 70 4 58 6 44 9 24 24 14 40 14c16 0 27 12 27 28 0 6-2 10-4 14l4 10h-6v12H50v16"/><circle cx="36" cy="44" r="16"/><path d="M36 56V44M36 46c-6 0-9-4-9-9 6 0 9 4 9 9zM36 44c0-6 4-9 9-9 0 6-4 9-9 9z"/></svg>
    Education</div>
</section>

<section class="abs band" style="top:1852px;height:164px">
  <h2 class="abs heading" style="left:248px;top:64px;font-size:22px;white-space:nowrap">Want us to work on your next project?</h2>
  <div class="btn" style="left:820px;top:61px;width:148px;height:41px">Contact us</div>
</section>

<section>
  <h2 class="abs heading center" style="top:2094px;font-size:29px">Featured Projects</h2>
  <div class="rule" style="top:2147px"></div>
  <div class="card-img" style="left:158px;background:linear-gradient(170deg,#8fb8e0,#d9dcd6 55%,#5e8a3a)" role="img" aria-label="House with solar panels on the roof and a green lawn"></div>
  <div class="card-img" style="left:458px;background:linear-gradient(170deg,#8d9590,#c4c8c3 50%,#6e7a72)" role="img" aria-label="Aerial view of rooftops covered with solar panels"></div>
  <div class="card-img" style="left:758px;background:linear-gradient(170deg,#3f7fd3,#8db8e8 50%,#b9b39a)" role="img" aria-label="Engineers in safety vests inspecting wind turbines"></div>
  <h3 class="card-title heading" style="left:158px">Lorem ipsum dolor sit</h3>
  <h3 class="card-title heading" style="left:458px">Lorem ipsum dolor sit</h3>
  <h3 class="card-title heading" style="left:758px">Lorem ipsum dolor sit</h3>
  <p class="card-text" style="left:158px">Lorem ipsum dolor sit amet, consectetur ut labore et dolore magna aliqua. Ut enim ad minim veniam, quis nostrud exercitation .</p>
  <p class="card-text" style="left:458px">Lorem ipsum dolor sit amet, consectetur adipisicing elit, sed do eiusmod tempor incididunt ut labore et dolore magna aliqua. Ut enim ad minim veniam, quis nostrud.</p>
  <p class="card-text" style="left:758px">Lorem ipsum dolor sit amet, consectetur adipisicing elit, sed do eiusmod tempor incididunt ut labore et dolore ullamco laboris nisi ut aliquip ex ea commodo consequat.</p>
  <div class="btn" style="left:521px;top:2551px;width:158px;height:40px">See more projects!</div>
</section>

<section class="abs band" style="top:2659px;height:164px">
  <h2 class="abs heading" style="left:107px;top:32px;font-size:23px;white-space:nowrap">Sign up for Sustainability Stories</h2>
  <p class="abs" style="left:107px;top:80px;width:420px;font-size:11.5px;line-height:20px">Get insights from people working with environmental issues every day. You'll receive our bi-monthly newsletter direct to your inbox.</p>
  <div class="field" style="left:566px;top:61px;width:170px">Name</div>
  <div class="field" style="left:744px;top:61px;width:207px">Email *</div>
  <div class="btn" style="left:959px;top:61px;width:106px;height:40px;font-weight:600">Signup</div>
</section>

<div class="abs mint-b"></div>
<section>
  <h2 class="abs heading center" style="top:2899px;font-size:29px">Latest News &amp; Blog</h2>
  <div class="rule" style="top:2950px"></div>
  <div class="news-img" style="left:179px;background:linear-gradient(150deg,#e9ecec,#b8c4c4)" role="img" aria-label="Hands reviewing charts on paper with a pen"></div>
  <div class="news-img" style="left:613px;background:linear-gradient(150deg,#dfe3e0,#9fb3ae)" role="img" aria-label="Person working at a desk with a laptop"></div>
  <h3 class="news-title" style="left:385px">Employment<br>opportunities.</h3>
  <h3 class="news-title" style="left:817px">What's new<br>at Tallis Australia</h3>
  <p class="news-text" style="left:385px">Lorem ipsum dolor sit amet, consectetur adipisicing elit, sed do eiusmod tempor incididunt ut labore et dolore magna aliqua. Ut enim ad minim veniam.</p>
  <p class="news-text" style="left:817px">Lorem ipsum dolor sit amet, consectetur adipisicing elit, sed do eiusmod tempor incididunt ut labore et dolore magna aliqua. Ut enim ad minim veniam.</p>
  <span class="news-more" style="left:385px">Read More +</span>
  <span class="news-more" style="left:817px">Read More +</span>
  <div class="btn" style="left:519px;top:3244px;width:162px;height:40px">See more blog posts!</div>
</section>

<section>
  <h2 class="abs heading center" style="top:3455px;font-size:29px">Our Clients &amp; Partners</h2>
  <div class="rule" style="top:3506px"></div>
  <p class="abs center" style="top:3528px;font-size:11.5px;color:#444">We work in partnership with our clients to embed sustainability within their projects and organisations.</p>
  <div class="clients">
    <div class="client"><i></i>Harbour Cover</div>
    <div class="client">Larkfield</div>
    <div class="client">Eastbay City</div>
    <div class="client"><i></i>Coastline Transit</div>
    <div class="client"><i></i>Vantel</div>
    <div class="client">ornix</div>
  </div>
</section>

<footer class="abs footer">
  <div class="f-label" style="left:147px;top:46px">Search</div>
  <div class="search">Type and hit enter</div>
  <div class="f-label" style="left:473px;top:46px">Recent posts</div>
  <div class="f-text" style="left:473px;top:78px;font-size:11px">Tallis Australia Races for Bird Conservation<br><span style="opacity:.85">January 5, 2019</span></div>
  <div class="f-label" style="left:818px;top:46px">Social media</div>
  <i class="dot" style="left:818px;top:80px"></i><i class="dot" style="left:851px;top:80px"></i><i class="dot" style="left:884px;top:80px"></i>

  <div class="f-city" style="left:147px;top:200px">Sydney</div>
  <i class="f-ico" style="left:147px;top:238px"></i>
  <div class="f-text" style="left:186px;top:238px">Level 4, 12 Harbour Parade<br>Seaview NSW 2099<br>Australia</div>
  <i class="f-ico" style="left:147px;top:312px"></i><div class="f-text" style="left:186px;top:314px">+61 2 5550 1420</div>
  <i class="f-ico" style="left:147px;top:348px"></i><div class="f-text" style="left:186px;top:350px">E-mail: hello@tallisworks.example</div>

  <div class="f-city" style="left:473px;top:200px">Melbourne</div>
  <i class="f-ico" style="left:473px;top:238px"></i>
  <div class="f-text" style="left:511px;top:238px">Level 2, 58 Elmwood Street,<br>Melbourne VIC 3001,<br>Australia</div>
  <i class="f-ico" style="left:473px;top:312px"></i><div class="f-text" style="left:511px;top:314px">+61 2 5550 1420</div>
  <i class="f-ico" style="left:473px;top:348px"></i><div class="f-text" style="left:511px;top:350px">E-mail: hello@tallisworks.example</div>

  <div class="f-city" style="left:818px;top:200px">Santiago</div>
  <i class="f-ico" style="left:818px;top:238px"></i>
  <div class="f-text" style="left:857px;top:238px">Avenida Los Robles 1480, Oficina 305<br>Las Condes<br>Chile</div>
  <i class="f-ico" style="left:818px;top:312px"></i><div class="f-text" style="left:857px;top:314px">+61 2 5550 1420</div>
  <i class="f-ico" style="left:818px;top:348px"></i><div class="f-text" style="left:857px;top:350px">E-mail: hello@tallisworks.example</div>

  <div class="f-text" style="left:142px;top:464px;font-size:11px">© Copyright 2019 Tallis Ecological Works. All right reserved.</div>
  <div class="f-links"><span>Terms</span><span>Privacy</span><span>Newsletter</span><span>Sitemap</span></div>
</footer>

</body>
</html>
```